KVT Building And Maintenance

Need a very professional looking double sided Buisiness card with all my details phone number, name, email, license number.

Target Market(s)

construction industry

Industry/Entity Type

building

Contact Information for Business Card

Name Dale Pemberton. Email Address Info@KVTBuilding.com.au mobile number 0452918736 licence number 671093D. web site

```html
<!DOCTYPE html>
<html lang="en">
<head>
<meta charset="utf-8">
<title>KVT Building And Maintenance – Business Card</title>
<link rel="stylesheet" href="https://fonts.googleapis.com/css2?family=Michroma&family=Poppins:wght@400;500;600&display=swap">
<style>
  :root {
    --page-bg: #e9e6e1;
    --card-white: #ffffff;
    --ink-dark: #3a3d42;
    --ink-body: #3f4246;
    --brand-blue: #2a9fdc;
    --rule-grey: #9a9ea3;
    --wood-light: #efe4d2;
    --wood-mid: #c9a57a;
    --wood-dark: #6b4a2e;
    --sky-blue: #5d86a8;
    --sky-warm: #f1c88a;
    --earth-dark: #3b2a1e;
    --white: #ffffff;
  }
  * { box-sizing: border-box; margin: 0; padding: 0; }
  html, body { width: 900px; height: 1200px; overflow: hidden; }
  body {
    background: var(--page-bg);
    position: relative;
    font-family: "Poppins", sans-serif;
  }
  .card {
    position: absolute;
    left: 95px;
    width: 710px;
    height: 416px;
    border-radius: 22px;
    overflow: hidden;
    box-shadow: 0 6px 14px rgba(0,0,0,0.25);
  }
  /* Front */
  .card-front { top: 130px; background: var(--card-white); }
  .front-photo {
    position: absolute;
    left: 290px; top: 0;
    width: 420px; height: 292px;
    background:
      linear-gradient(90deg, var(--card-white) 0%, rgba(255,255,255,0) 35%),
      linear-gradient(160deg, var(--wood-light) 0%, var(--wood-mid) 55%, var(--wood-dark) 100%);
  }
  .brand-name {
    position: absolute;
    left: 47px; top: 74px;
    display: flex; align-items: center; gap: 12px;
    font-family: "Michroma", sans-serif;
    font-size: 17px;
    line-height: 1.15;
    color: var(--ink-dark);
    text-transform: uppercase;
  }
  .brand-mark {
    width: 20px; height: 20px;
    background: var(--brand-blue);
    flex: none;
  }
  .holder-name {
    position: absolute;
    left: 47px; top: 262px;
    font-family: "Michroma", sans-serif;
    font-size: 19px;
    letter-spacing: 1px;
    color: var(--ink-dark);
    text-transform: uppercase;
  }
  .holder-name .surname { color: var(--brand-blue); }
  .front-rule {
    position: absolute;
    left: 47px; top: 292px;
    width: 663px; height: 1px;
    background: var(--rule-grey);
  }
  .contact-list {
    position: absolute;
    left: 46px; top: 301px;
    list-style: none;
    font-size: 15.5px;
    color: var(--ink-body);
  }
  .contact-list li {
    display: flex; align-items: center; gap: 8px;
    height: 23.5px;
  }
  .contact-list svg { width: 15px; height: 15px; flex: none; }
  .licence {
    position: absolute;
    right: 38px; top: 347px;
    font-size: 15.5px;
    color: var(--ink-body);
  }
  /* Back */
  .card-back {
    top: 601px;
    background:
      linear-gradient(180deg, rgba(0,0,0,0) 55%, var(--earth-dark) 100%),
      radial-gradient(ellipse at 52% 68%, var(--sky-warm) 0%, rgba(241,200,138,0) 45%),
      linear-gradient(180deg, var(--sky-blue) 0%, #9fb3c2 50%, #c9a07a 75%, var(--earth-dark) 100%);
  }
  .back-brand {
    position: absolute;
    left: 0; right: 0; top: 178px;
    display: flex; justify-content: center; align-items: center; gap: 14px;
    font-family: "Michroma", sans-serif;
    font-size: 26px;
    line-height: 1.1;
    color: var(--white);
    text-transform: uppercase;
  }
  .back-brand .brand-mark { width: 28px; height: 28px; }
  .back-web {
    position: absolute;
    left: 0; right: 0; top: 372px;
    text-align: center;
    font-weight: 600;
    font-size: 15px;
    letter-spacing: 1.5px;
    color: var(--white);
  }
</style>
</head>
<body>
  <section class="card card-front">
    <div class="front-photo" role="img" aria-label="Photo of a builder in hard hat and tool belt working among timber roof trusses"></div>
    <div class="brand-name">
      <span class="brand-mark"></span>
      <span>KVT Building and<br>Maintenance</span>
    </div>
    <div class="holder-name">Dale <span class="surname">Pemberton</span></div>
    <div class="front-rule"></div>
    <ul class="contact-list">
      <li>
        <svg viewBox="0 0 16 16" aria-hidden="true"><path d="M4 1.5l2.2 3-1.3 1.6a8 8 0 0 0 5 5l1.6-1.3 3 2.2-1.2 2.3C8 14.5 1.5 8 1.7 2.7z" fill="none" stroke="#2a9fdc" stroke-width="1.4" stroke-linejoin="round"/></svg>
        0452918736
      </li>
      <li>
        <svg viewBox="0 0 16 16" aria-hidden="true"><rect x="1" y="3" width="14" height="10" fill="#2a9fdc"/><path d="M1 3l7 5.5L15 3" fill="none" stroke="#fff" stroke-width="1.2"/></svg>
        Info@KVTBuilding.com.au
      </li>
      <li>
        <svg viewBox="0 0 16 16" aria-hidden="true"><g fill="none" stroke="#2a9fdc" stroke-width="1.2"><circle cx="8" cy="8" r="6.5"/><ellipse cx="8" cy="8" rx="3" ry="6.5"/><path d="M1.5 8h13M2.5 4.5h11M2.5 11.5h11"/></g></svg>
        KVTBuilding.com.au
      </li>
    </ul>
    <div class="licence">licence number : 671093D</div>
  </section>

  <section class="card card-back" role="img" aria-label="Photo of an excavator digging earth against a sunset sky with a dump truck in the distance">
    <div class="back-brand">
      <span class="brand-mark"></span>
      <span>KVT Building and<br>Maintenance</span>
    </div>
    <div class="back-web">KVTBUILDING.COM.AU</div>
  </section>
</body>
</html>
```